Varnelux7 website

Need to create a website for my business

Target Market(s)

Food ingredient companies, B2B

Industry/Entity Type

Food technology, food ingredients

Coding

Number of Pages Required

2 page

Requirements
Nice to have
• Case studies, links to articles,

```html
<!DOCTYPE html>
<html lang="en">
<head>
<meta charset="utf-8">
<title>Varnelux7 — Business Advice for Food Ingredients</title>
<link rel="stylesheet" href="https://fonts.googleapis.com/css2?family=Poppins:wght@300;400;500;600;700&display=swap">
<style>
:root{
  --green:#17861f;
  --green-dark:#0f6d16;
  --ink:#1d1d1d;
  --muted:#6b6b6b;
  --grey-band:#f1f1f1;
  --footer:#2a2a2a;
  --white:#ffffff;
  --photo-warm:#d9b99a;
  --photo-cool:#b7c3c9;
}
*{box-sizing:border-box;margin:0;padding:0}
html,body{width:1200px;height:3592px;overflow:hidden}
body{position:relative;background:var(--white);font-family:"Poppins",sans-serif;color:var(--ink)}
.abs{position:absolute}
a{color:inherit;text-decoration:none}

/* header */
.site-header{left:0;top:0;width:1200px;height:64px}
.brand{left:88px;top:12px;display:flex;align-items:center;gap:10px}
.brand-dot{width:26px;height:26px;border-radius:50%;background:var(--green)}
.brand-name{font-size:22px;font-weight:600;letter-spacing:2px;color:var(--ink);line-height:1}
.brand-tag{font-size:9px;color:var(--muted);margin-top:3px;letter-spacing:.3px}
.main-nav{right:88px;top:20px;display:flex;align-items:center;gap:26px;font-size:11px;font-weight:600;text-transform:uppercase}
.nav-home{width:12px;height:12px;background:var(--green);clip-path:polygon(50% 0,100% 45%,85% 45%,85% 100%,15% 100%,15% 45%,0 45%)}
.nav-cta{border:2px solid var(--green);border-radius:20px;padding:6px 16px}

/* hero */
.hero-eyebrow{left:88px;top:288px;font-size:13px;font-weight:600;color:var(--green);letter-spacing:1px}
.hero-title{left:88px;top:310px;font-size:50px;font-weight:600;line-height:54px;width:480px}
.hero-sub{left:88px;top:426px;font-size:17px;color:var(--ink)}
.btn-green{background:var(--green);color:var(--white);font-size:10px;font-weight:600;border-radius:20px;padding:10px 22px;letter-spacing:.5px}
.hero-cta{left:88px;top:474px}
.hero-photo{left:610px;top:110px;width:500px;height:410px;border-radius:120px 0 40px 0;background:linear-gradient(135deg,var(--photo-cool),#e8d3b3 55%,#c9743b)}

/* about */
.about-photo{left:140px;top:720px;width:450px;height:430px;border-radius:90px 0 0 40px;background:linear-gradient(160deg,#cfd2d0,#e6e2da 50%,#8c6a4a)}
.about-panel{left:590px;top:830px;width:480px;height:450px;background:var(--green);border-radius:50px 50px 50px 0;color:var(--white);padding:120px 0 0 72px}
.about-eyebrow{font-size:11px;font-weight:500;letter-spacing:1px}
.about-title{font-size:40px;font-weight:600;line-height:48px}
.about-text{font-size:11px;line-height:17px;width:260px;margin-top:6px}
.btn-outline{display:inline-block;margin-top:22px;border:2px solid var(--white);border-radius:20px;font-size:10px;font-weight:600;padding:8px 16px}

/* consulting */
.consulting{left:0;top:1250px;width:1200px;height:590px;background:var(--grey-band)}
.section-eyebrow{width:1200px;text-align:center;font-size:11px;font-weight:500;letter-spacing:1px}
.section-title{width:1200px;text-align:center;font-size:54px;font-weight:500;line-height:62px}
.section-sub{width:1200px;text-align:center;font-size:12px;color:var(--muted)}
.sector{width:144px;text-align:center}
.sector-card{width:144px;height:144px;border-radius:14px;background:var(--white);display:flex;align-items:center;justify-content:center;box-shadow:0 4px 14px rgba(0,0,0,.06)}
.sector-card.active{background:var(--green)}
.sector-icon{width:62px;height:62px;border-radius:12px;background:#d6d6d6}
.sector-card.active .sector-icon{background:#5fb265}
.sector-label{font-size:13px;margin-top:14px}

/* case studies */
.case-card{width:240px;height:318px;background:var(--white);border-radius:14px;box-shadow:0 6px 20px rgba(0,0,0,.08);overflow:hidden}
.case-photo{height:170px;width:100%}
.case-body{padding:14px 16px}
.case-title{font-size:13px;font-weight:600}
.case-text{font-size:10px;line-height:15px;color:var(--muted);margin-top:6px}
.read-more{font-size:10px;font-weight:700;color:var(--green);margin-top:10px;display:block}

/* news */
.news-card{width:336px}
.news-photo{height:232px;border-radius:14px 14px 14px 0}
.news-date{font-size:11px;color:var(--muted);margin-top:14px;display:flex;gap:8px;align-items:center}
.news-date::before{content:"";width:10px;height:10px;border:2px solid var(--green);border-radius:2px}
.news-title{font-size:15px;font-weight:600;line-height:20px;margin-top:4px}

/* footer */
.footer-bg{left:0;top:2900px}
.newsletter{left:88px;top:2980px;width:1024px;height:180px;background:var(--green);border-radius:30px 30px 30px 0;color:var(--white)}
.newsletter-title{left:56px;top:48px;font-size:38px;font-weight:500}
.newsletter-sub{left:58px;top:100px;font-size:13px}
.newsletter-form{left:474px;top:65px;width:480px;height:46px;background:var(--white);border-radius:24px;color:var(--muted);font-size:13px;padding:14px 22px}
.send-icon{right:18px;top:14px}
.footer-brand{left:88px;top:3290px}
.footer-brand .brand-name{color:var(--white);font-size:20px}
.footer-brand .brand-tag{color:#cfcfcf}
.footer-col{top:3280px;color:var(--white)}
.footer-col h4{font-size:16px;font-weight:600;margin-bottom:12px}
.footer-col li{list-style:none;font-size:11px;line-height:19px;color:#d7d7d7}
.contact-item{display:flex;align-items:center;gap:10px}
.contact-item::before{content:"";width:7px;height:7px;border-radius:50%;background:var(--green)}
.copyright{left:0;top:3548px;width:1200px;text-align:center;font-size:12px;color:#d7d7d7}
.to-top{left:1116px;top:3530px;width:30px;height:30px;border-radius:50%;background:var(--green)}
</style>
</head>
<body>

<header class="abs site-header">
  <div class="abs brand">
    <span class="brand-dot"></span>
    <div><div class="brand-name">VARNELUX7</div><div class="brand-tag">Results Matter. Work hard.</div></div>
  </div>
  <nav class="abs main-nav">
    <span class="nav-home"></span>
    <a href="#">About Us</a><a href="#">Case Studies</a><a href="#">Services</a><a href="#">Blog</a>
    <a href="#" class="nav-cta">Contact Us</a>
  </nav>
</header>

<section>
  <div class="abs hero-eyebrow">VARNELUX7</div>
  <h1 class="abs hero-title">Expert In Business Advice</h1>
  <p class="abs hero-sub">Result Matter Work hand</p>
  <a href="#" class="abs btn-green hero-cta">CONTACT US TODAY</a>
  <div class="abs hero-photo" role="img" aria-label="Woman with a tablet beside a table of fresh vegetables and fruit"></div>
</section>

<section>
  <div class="abs about-photo" role="img" aria-label="Two chefs preparing food in a professional kitchen"></div>
  <div class="abs about-panel">
    <div class="about-eyebrow">CONSULTANT</div>
    <h2 class="about-title">About Us</h2>
    <p class="about-text">Varnelux7 Consulting is a business to business marketing and consulting firm specializing in the food, food ingredients and biotech sectors.</p>
    <a href="#" class="btn-outline">READ MORE</a>
  </div>
</section>

<section class="abs consulting">
  <div class="abs section-eyebrow" style="top:96px">VARNELUX7</div>
  <h2 class="abs section-title" style="top:108px">Consulting</h2>
  <p class="abs section-sub" style="top:186px">We cover a range of industries as diverse as these...</p>
  <div class="abs sector" style="left:272px;top:280px"><div class="sector-card"><div class="sector-icon" role="img" aria-label="Ingredients icon"></div></div><div class="sector-label">Ingredients</div></div>
  <div class="abs sector" style="left:440px;top:280px"><div class="sector-card active"><div class="sector-icon" role="img" aria-label="Nutraceuticals icon"></div></div><div class="sector-label">Nutraceuticals</div></div>
  <div class="abs sector" style="left:608px;top:280px"><div class="sector-card"><div class="sector-icon" role="img" aria-label="Pharmaceuticals icon"></div></div><div class="sector-label">Pharmaceuticals</div></div>
  <div class="abs sector" style="left:776px;top:280px"><div class="sector-card"><div class="sector-icon" role="img" aria-label="Food and nutrition icon"></div></div><div class="sector-label">Food &amp; Nutrition</div></div>
</section>

<section>
  <h2 class="abs section-title" style="top:1950px;font-size:50px">Case Studies</h2>
  <article class="abs case-card" style="left:88px;top:2044px">
    <div class="case-photo" role="img" aria-label="Team meeting in an office" style="background:linear-gradient(135deg,#a97b58,#e3cdb2)"></div>
    <div class="case-body"><h3 class="case-title">Regulatory advice</h3><p class="case-text">Our global regulatory teams can help you with all aspects of food &amp; beverage regulations.</p><a href="#" class="read-more">READ MORE</a></div>
  </article>
  <article class="abs case-card" style="left:349px;top:2044px">
    <div class="case-photo" role="img" aria-label="Worker in a food production facility" style="background:linear-gradient(135deg,#8fa3b3,#dfe5ea)"></div>
    <div class="case-body"><h3 class="case-title">Food safety</h3><p class="case-text">Our safety specialists help you audit plants and keep every batch within strict standards.</p><a href="#" class="read-more">READ MORE</a></div>
  </article>
  <article class="abs case-card" style="left:610px;top:2044px">
    <div class="case-photo" role="img" aria-label="Roasted chicken dish on a dark table" style="background:linear-gradient(135deg,#3d2a20,#b86a33)"></div>
    <div class="case-body"><h3 class="case-title">Product innovation</h3><p class="case-text">Our product teams guide you from first concept to launch of new food &amp; beverage lines.</p><a href="#" class="read-more">READ MORE</a></div>
  </article>
  <article class="abs case-card" style="left:871px;top:2044px">
    <div class="case-photo" role="img" aria-label="Nutrition supplement packaging" style="background:linear-gradient(135deg,#9a5ea8,#e8dde8)"></div>
    <div class="case-body"><h3 class="case-title">Membership</h3><p class="case-text">Our member network gives you access to insights, events and peers across the food sector.</p><a href="#" class="read-more">READ MORE</a></div>
  </article>
</section>

<section>
  <h2 class="abs section-title" style="top:2466px;font-size:50px">What's new?</h2>
  <article class="abs news-card" style="left:88px;top:2560px">
    <div class="news-photo" role="img" aria-label="Chefs plating food in a kitchen" style="background:linear-gradient(135deg,#b9a89a,#5c4537)"></div>
    <div class="news-date">08 Apr 2022</div>
    <h3 class="news-title">Northmeal Foods Recognizes Chef Partners Group</h3>
  </article>
  <article class="abs news-card" style="left:432px;top:2560px">
    <div class="news-photo" role="img" aria-label="Restaurant dining room with staff" style="background:linear-gradient(135deg,#6d4a33,#c99a6b)"></div>
    <div class="news-date">08 Apr 2022</div>
    <h3 class="news-title">New Business Relationship with company name</h3>
  </article>
  <article class="abs news-card" style="left:776px;top:2560px">
    <div class="news-photo" role="img" aria-label="Bowls of food on a table seen from above" style="background:linear-gradient(135deg,#2c2420,#8a6a4a)"></div>
    <div class="news-date">08 Apr 2022</div>
    <h3 class="news-title">Canadian Culinary Immersion With Friends</h3>
  </article>
</section>

<footer>
  <svg class="abs footer-bg" width="1200" height="692" viewBox="0 0 1200 692" aria-hidden="true">
    <path d="M0 170 C260 70 520 30 760 30 L1200 0 L1200 692 L0 692 Z" fill="var(--footer)"/>
  </svg>
  <div class="abs newsletter">
    <h2 class="abs newsletter-title">Newsletter</h2>
    <p class="abs newsletter-sub">Subscribe to our newsletter</p>
    <div class="abs newsletter-form">Enter your email
      <svg class="abs send-icon" width="18" height="18" viewBox="0 0 24 24" aria-hidden="true"><path d="M2 21 23 12 2 3v7l15 2-15 2z" fill="var(--ink)"/></svg>
    </div>
  </div>
  <div class="abs brand footer-brand">
    <span class="brand-dot"></span>
    <div><div class="brand-name">VARNELUX7</div><div class="brand-tag">Results Matter. Work hard.</div></div>
  </div>
  <div class="abs footer-col" style="left:384px">
    <h4>Our Studies</h4>
    <ul><li>Nutrition</li><li>Nutraceuticals</li><li>Ingredients</li><li>Dairy Ingredients</li><li>Flavors &amp; Colorings</li></ul>
  </div>
  <div class="abs footer-col" style="left:604px">
    <h4>Quick Links</h4>
    <ul><li>Home</li><li>About us</li><li>Case Studies</li><li>Sitemap</li><li>Contact</li></ul>
  </div>
  <div class="abs footer-col" style="left:820px">
    <h4>Contact us</h4>
    <ul><li class="contact-item">Some goes address here</li><li class="contact-item">info@varnelux7.com</li><li class="contact-item">+1 555 010 2040</li></ul>
  </div>
  <p class="abs copyright">©Copyright 2022 | All Rights Reserved</p>
  <a href="#" class="abs to-top" aria-label="Back to top"></a>
</footer>

</body>
</html>
```